Packaging and labelling for Swiss made Organic CBD Oil

Visit our website www.velmoraoils.example
We have not put any product on yet as require packaging and label design .
Website will give you a great feel for the company and how we have used
the logo . The Brastek cbd product shown is a company similar to ourselves with similar core values , we liked the clean packaging design they have .

Im happy if you want use the mandala symbol in our logo separate from
VELMORA, to separate and use the mandala symbol as a larger icon than
it appears in our logo
Clean , Pure , organic feel. Like the product to look pharmaceutical and life changing not gimmicky.
Colours to go with or be the same as our logo colours
But not too cold and clinical
Bottle size 84mm x 25mm
Label size 75mm x 30mm
Box 30mm x 30mm x 100mm
6 products
Full Spectrum :
500mg CBD (5%)
1000mg CBD ( 10% )
1500mg CBD (15%)
2000mg CBD ( 20% )
Broad spectrum THC Free
500mg CBD (5%)
Pets
500mg Broad Spectrum THC Free
Updates

Would like the design to be more modern than traditional

LABEL Information Front of Bottle - Logo VELMORA & Mandala - Mandala can be used separately as design symbol Organic Cannabis Oil 1500mg CBD (15%) Ful Spectrum 10ml Back of bottle Ingredients: Organic Cannabis Oil Extract Organic Sunflower Seed Oil THC - 0.2% Certified Swiss Organic Cultivation Shake well before use. Store in a cool , dry place and out of the each of children BOX information Front and rear Logo - VELMORA & Mandala - Mandala can be used separately as a design symbol Organic Cannabis Oil 1500mg CBD (15%) Full Spectrum Sides x 2 This product is a food supplement and is not intended to diagnose, treat, cure or prevent any disease If you are pregnant, lactating or taking any medication consult your health care practitioner Suitable for vegetarians and vegans Ingredients Organic Cannabis Oil extract Organis Sunflower Oil Store in a cool ,dry place, out of the reach of children Recommended Use 1-5 drops ( 1 drop = 7.5mg CBD ) Subject to body weight and personal requirement - visit www.velmoraoils for more information 100% Natural 100% Organic GMO free 100% Vegan ( symbol with each ) Expiry date see bottle label Cultivated and manufactured in Switzerland

Target Market(s)

age 40 - 80

Font styles to use
Other font styles liked:
• In our website we have used Open Sans for the copy and Lato for headings .

Requirements
Must have
• look like an Industry leader
Velmora will change the quality of peoples lives and in some cases may
even save lives so want look powerful and credible
Our Mission is - Through Delivering Pure , Premium , Organic products we will educate, inform and help people achieve healthier , happier lifestyles
Nice to have
• Colours to look good with our logo colours or be the same as our logo
colours
Logo Font - Avenir Black and Avenir Book

Font used in website - Content - Open Sans / Headings - Lato
If you have another font for the packaging information that will go well with
our logo, I'm happy for you to use your skills

```html
<!DOCTYPE html>
<html lang="en">
<head>
<meta charset="utf-8">
<title>Velmora Full Spectrum CBD Oil – Box and Label</title>
<link rel="stylesheet" href="https://fonts.googleapis.com/css2?family=Mulish:wght@300;400;600;700&family=Open+Sans:wght@400;600&display=swap">
<style>
  :root{
    --bg:#e4e5e7;
    --teal:#0f4b54;
    --teal-edge:#0b3d45;
    --mint:#a9ddd6;
    --white:#ffffff;
    --soft:#d7ecea;
    --head:"Mulish", sans-serif;
    --copy:"Open Sans", sans-serif;
  }
  *{box-sizing:border-box;margin:0;padding:0}
  html,body{width:1200px;height:1200px;overflow:hidden;background:var(--bg)}
  body{position:relative;font-family:var(--copy);color:var(--white)}

  .dieline{position:absolute;left:130px;top:50px;display:flex;height:790px}
  .panel{position:relative;background:var(--teal);border-right:1px solid var(--teal-edge);
         display:flex;flex-direction:column;align-items:center}
  .panel:last-child{border-right:none}
  .panel--side{width:200px;padding:42px 18px 36px}
  .panel--main{width:270px;padding:42px 22px 36px}

  .brand{display:flex;align-items:center;gap:8px;font-family:var(--head);font-weight:700;
         letter-spacing:3px;color:var(--white);line-height:1}
  .brand__dot{width:10px;height:10px;border-radius:50%;background:var(--mint)}
  .panel--main .brand{font-size:28px}
  .panel--side .brand{font-size:22px}

  .emblem-space{border:2px solid var(--mint);border-radius:50%}
  .panel--main .emblem-space{width:150px;height:150px;margin:62px 0 0}
  .panel--side .emblem-space{width:110px;height:110px;margin:52px 0 0}

  .product-name{font-family:var(--head);text-align:center;line-height:1.05}
  .product-name__kind{display:block;font-weight:700}
  .product-name__type{display:block;font-weight:300}
  .panel--main .product-name{margin-top:120px}
  .panel--main .product-name__kind{font-size:22px}
  .panel--main .product-name__type{font-size:44px}
  .panel--side .product-name{margin-top:108px}
  .panel--side .product-name__kind{font-size:17px}
  .panel--side .product-name__type{font-size:34px}

  .strength{position:relative;border:2px solid var(--soft);text-align:center;font-family:var(--head)}
  .strength__top,.strength__bottom{position:absolute;left:50%;transform:translateX(-50%);
         background:var(--teal);padding:0 6px;font-weight:300;white-space:nowrap;color:var(--soft)}
  .strength__amount{font-weight:700;display:block}
  .panel--main .strength{margin-top:40px;width:184px;padding:20px 0 18px}
  .panel--main .strength__top,.panel--main .strength__bottom{font-size:19px}
  .panel--main .strength__top{top:-13px}
  .panel--main .strength__bottom{bottom:-13px}
  .panel--main .strength__amount{font-size:22px}
  .panel--side .strength{margin-top:34px;width:140px;padding:16px 0 14px}
  .panel--side .strength__top,.panel--side .strength__bottom{font-size:15px}
  .panel--side .strength__top{top:-11px}
  .panel--side .strength__bottom{bottom:-11px}
  .panel--side .strength__amount{font-size:17px}

  .volume{font-family:var(--head);font-weight:700}
  .panel--main .volume{margin-top:62px;font-size:18px}
  .panel--side .volume{margin-top:50px;font-size:15px}
  .origin{margin-top:auto;font-family:var(--head);font-weight:400}
  .panel--main .origin{font-size:16px}
  .panel--side .origin{font-size:13px}

  .notice{width:100%;border:1px solid var(--soft);padding:10px 9px 9px;position:relative;
          font-size:9.5px;line-height:1.45;color:var(--soft)}
  .notice__title{position:absolute;left:-1px;top:-12px;background:var(--soft);color:var(--teal);
          font-size:7.5px;font-weight:600;padding:2px 5px;letter-spacing:.3px}
  .side-info{margin-top:210px;width:100%;display:flex;flex-direction:column;gap:36px}
  .side-info__about{font-size:9.5px;line-height:1.5;color:var(--soft)}

  .back-copy{margin-top:110px;width:100%}
  .back-copy__title{font-family:var(--head);font-weight:700;font-size:19px;margin-bottom:8px}
  .back-copy__text{font-size:12px;line-height:1.42;text-align:justify;color:var(--soft)}
  .batch{margin-top:92px;width:100%;font-family:var(--head);font-size:16px;line-height:1.75}
  .batch__line{display:inline-block;width:70px;border-bottom:1px solid var(--soft);margin-left:2px}

  .label{position:absolute;left:250px;top:880px;width:700px;height:280px;background:var(--teal);
         display:flex;flex-direction:column;align-items:center;padding:28px 0 22px}
  .label .brand{font-size:26px}
  .label .emblem-space{width:78px;height:78px;margin-top:16px}
  .label .strength{margin-top:26px;width:176px;padding:14px 0 12px}
  .label .strength__top,.label .strength__bottom{font-size:16px}
  .label .strength__top{top:-11px}
  .label .strength__bottom{bottom:-11px}
  .label .strength__amount{font-size:20px}
  .label .volume{margin-top:18px;font-size:15px}
  .label .origin{font-size:13px;margin-top:8px}
</style>
</head>
<body>

<section class="dieline" aria-label="Box flat layout">
  <div class="panel panel--side">
    <div class="brand">VELMORA</div>
    <div class="side-info">
      <div class="notice"><span class="notice__title">DO NOT REFRIGERATE</span>Keep at room temperature to preserve freshness. Store away from humidity, heat, and light.</div>
      <div class="notice"><span class="notice__title">WARNING</span>If pregnant, nursing or taking prescription drugs, consult your physician prior to use. Keep out of reach of children.</div>
      <p class="side-info__about">We are proud to say that our CBD products are high quality Swiss made using a combination of traditional and innovative techniques from the Swiss Alps.</p>
    </div>
  </div>

  <div class="panel panel--main">
    <div class="brand">VELMORA</div>
    <div class="emblem-space" role="img" aria-label="Brand emblem area"></div>
    <h1 class="product-name"><span class="product-name__kind">FULL SPECTRUM</span><span class="product-name__type">CBD OIL</span></h1>
    <div class="strength"><span class="strength__top">Organic CBD</span><span class="strength__amount">2000mg (20%)</span><span class="strength__bottom">THC Free</span></div>
    <p class="volume">1 FL OZ (30ml)</p>
    <p class="origin">Made in Swiss</p>
  </div>

  <div class="panel panel--side">
    <div class="brand">VELMORA</div>
    <div class="emblem-space" role="img" aria-label="Brand emblem area"></div>
    <h2 class="product-name"><span class="product-name__kind">FULL SPECTRUM</span><span class="product-name__type">CBD OIL</span></h2>
    <div class="strength"><span class="strength__top">Organic CBD</span><span class="strength__amount">2000mg (20%)</span><span class="strength__bottom">THC Free</span></div>
    <p class="volume">1 FL OZ (30ml)</p>
    <p class="origin">Made in Swiss</p>
  </div>

  <div class="panel panel--main">
    <div class="brand">VELMORA</div>
    <div class="emblem-space" role="img" aria-label="Brand emblem area"></div>
    <div class="back-copy">
      <h3 class="back-copy__title">100% organic</h3>
      <p class="back-copy__text">Providing the purest CBD oil is something that we take very seriously we make no compromises with the ingredients of our CBD oils. The majority of CBD oils available are produced by companies buying large quantities of (biomass) dried cannabis leaves and stems from unspecified growers around Europe and the USA.</p>
    </div>
    <div class="batch">Batch ID:<span class="batch__line"></span><br>Expiration Date:<span class="batch__line"></span></div>
  </div>
</section>

<section class="label" aria-label="Bottle label">
  <div class="brand">VELMORA</div>
  <div class="emblem-space" role="img" aria-label="Brand emblem area"></div>
  <div class="strength"><span class="strength__top">Organic CBD</span><span class="strength__amount">2000mg (20%)</span><span class="strength__bottom">THC Free</span></div>
  <p class="volume">1 FL OZ (30ml)</p>
  <p class="origin">Made in Swiss</p>
</section>

</body>
</html>
```